One of a Kind Clean Business Card

We need to design a new business card template for our company. Our company designs and produced merchandising displays. You can see a sample of what we produce on our site www.qorvatrim.com. I have uploaded our logo in vector format, as well as a picture of our current business cards. We want a totally different look. We want simple and clean, looking forward to seeing what people create.
Updates

I would like to update the address for Teblo Displays 418 N Harlow Ln Brookvale, WI 60117 Would also note. No QR codes

Industry/Entity Type

Business

Contact Information for Business Card

Need a 1 sided business card designed.

Font styles to use
Serif

Requirements
Must have
• Easy to view; Clean Design
Nice to have
• Features that promote engineering and creativity
Should not have
• Too much clutter, keep it simple

```html
<!DOCTYPE html>
<html lang="en">
<head>
<meta charset="utf-8">
<title>Teblo Displays — Business Card</title>
<link rel="stylesheet" href="https://fonts.googleapis.com/css2?family=Open+Sans:wght@300;400;700&display=swap">
<style>
  :root {
    --backdrop: #e9e7e3;
    --card: #ffffff;
    --accent: #a3202c;
    --muted: #3a3a3a;
  }
  * { box-sizing: border-box; margin: 0; padding: 0; }
  html, body {
    width: 1200px; height: 1022px; overflow: hidden;
    background: var(--backdrop);
    font-family: "Open Sans", Arial, sans-serif;
  }
  .stage {
    width: 1200px; height: 1022px;
    display: flex; align-items: center; justify-content: center;
  }
  .card {
    position: relative;
    width: 1000px; height: 570px;
    background: var(--card);
    box-shadow: 0 2px 10px rgba(0,0,0,0.12);
    overflow: hidden;
  }
  .brand-name {
    position: absolute; left: 92px; top: 150px;
    font-weight: 300; font-size: 44px; line-height: 1.15;
    color: var(--accent);
  }
  .rule-main {
    position: absolute; left: 0; top: 300px;
    width: 930px; height: 3px; background: var(--accent);
  }
  .rule-tick {
    position: absolute; left: 330px; top: 300px;
    width: 3px; height: 260px; background: var(--accent);
  }
  .person {
    position: absolute; right: 70px; top: 246px;
    font-weight: 700; font-size: 34px; line-height: 48px; color: var(--accent);
  }
  .address {
    position: absolute; right: 70px; top: 318px;
    text-align: right;
    font-size: 24px; line-height: 34px; color: var(--muted);
  }
  .contacts {
    position: absolute; left: 352px; top: 398px;
    list-style: none;
  }
  .contacts li {
    display: flex; align-items: center; gap: 14px;
    font-size: 24px; line-height: 38px; color: var(--muted);
  }
  .contacts svg { width: 20px; height: 20px; flex: none; }
  .contacts svg * { stroke: var(--accent); fill: none; stroke-width: 2; }
  .contacts svg .solid { fill: var(--accent); stroke: none; }
</style>
</head>
<body>
<main class="stage">
  <article class="card">
    <p class="brand-name">Teblo Displays</p>

    <div class="rule-main"></div>
    <div class="rule-tick"></div>

    <h1 class="person">Dana Korver</h1>
    <p class="address">418 N Harlow<br>Ln Brookvale, WI 60117</p>

    <ul class="contacts">
      <li>
        <svg viewBox="0 0 20 20" aria-hidden="true"><path class="solid" d="M5 2l3 3-2 2c1 3 4 6 7 7l2-2 3 3-2 3C9 18 2 11 2 4z"/></svg>
        815-555-0142
      </li>
      <li>
        <svg viewBox="0 0 20 20" aria-hidden="true"><rect x="5" y="2" width="10" height="16" rx="2"/></svg>
        312-555-0176
      </li>
      <li>
        <svg viewBox="0 0 20 20" aria-hidden="true"><rect class="solid" x="1" y="4" width="18" height="12"/><path d="M1 4l9 7 9-7" style="stroke:#fff"/></svg>
        dkorver@qorvatrim.com
      </li>
      <li>
        <svg viewBox="0 0 20 20" aria-hidden="true"><circle cx="10" cy="10" r="8"/><path d="M2 10h16M10 2c-4 4-4 12 0 16M10 2c4 4 4 12 0 16"/></svg>
        www.qorvatrim.com
      </li>
    </ul>
  </article>
</main>
</body>
</html>
```